Home page design for a New Zealand clothing business

- The design must be based around the attached HPID (home page information design) called Copper Ridge HPID. I've attached Word and PDF versions - these are the same. The table boxes are just for approximate placement of information – you DON'T have to make it look exactly like this. All fonts used in the HPID are only examples - you can use any Google font you wish.

- Information only is in orange text. Copy to go on the design in black text. Some instructions are in the HPID. Please be creative!

- The design needs to be modern. Colours are to be mainly black and white (like the logo) and the accent colour is to be brown.

- I've provided the images for the galleries - they are labelled and will match the name in the HPID.

- One possibility is to have a large background image for the whole design. I've added one example image for this: NZ landscape background image.jpg You could supply one of your designs on a white background, and one on this landscape background.

- These are some websites that are similar with the products they sell. Please DON'T copy these sites but they are good examples....
http://www.tolmerapparel.co.nz/
http://www.quillet.co.nz/
http://www.vornak.co.nz/
http://www.pelhurst.co.nz/

Width of content will be 1100 pixels when implemented as a web page. Header height (without nav bar) 150-160 pixels.

The winning PSD file will have to be provided as follows…
1. Canvas size of 2000px x 2000px - 72ppi in Adobe Photoshop (CS5 compatible)
2. Width of content section is 1100px wide - centered in the canvas
3. Any button rollovers/hovers in the PSD as hidden layers.
4. All fonts used must be Google fonts (except for the fonts in the header at the top of the page).
5. You will need to supply the chosen home page plus one example page (example page as a style guide for how all other pages will look). Example page is only the header and navigational bar at the top, an empty sector in the middle with a column (180 px wide) which can be left or right aligned which means the main sector is 920 pixels wide, and then the footer at the bottom of the page

```html
<!DOCTYPE html>
<html lang="en">
<head>
<meta charset="utf-8">
<title>Copper Ridge – Traditional oilskin &amp; woollen clothing</title>
<link rel="stylesheet" href="https://fonts.googleapis.com/css2?family=Tinos:wght@400;700&family=Open+Sans:wght@400;600&display=swap">
<style>
  :root {
    --black: #000000;
    --white: #ffffff;
    --copper: #c0651f;
    --copper-dark: #a9561a;
    --ink: #111111;
    --grey-sky: #a9b0a8;
    --field: #7d9a4e;
    --serif: "Tinos", "Times New Roman", serif;
    --sans: "Open Sans", "Verdana", sans-serif;
  }
  * { box-sizing: border-box; margin: 0; padding: 0; }
  html, body { width: 1200px; height: 1200px; overflow: hidden; background: var(--white); }
  body { position: relative; font-family: var(--sans); color: var(--ink); }
  .abs { position: absolute; }

  /* Header */
  .brand { left: 277px; top: 22px; width: 160px; height: 78px; display: flex; align-items: center; gap: 8px; }
  .brand-dot { width: 22px; height: 22px; border-radius: 50%; background: var(--black); flex: none; }
  .brand-name { font-family: var(--serif); font-weight: 700; font-size: 25px; line-height: 1; color: var(--black); letter-spacing: 0.5px; }
  .tagline { left: 440px; top: 12px; width: 375px; text-align: center; font-family: var(--serif); font-size: 22px; color: var(--black); }
  .offers { left: 480px; top: 48px; width: 295px; text-align: center; font-family: var(--serif); color: var(--copper); font-size: 14.5px; line-height: 20px; }
  .offers .phone { font-size: 18px; line-height: 22px; }
  .search { left: 784px; top: 87px; display: flex; align-items: center; gap: 16px; font-family: var(--serif); font-size: 9px; color: var(--black); }
  .search-box { width: 96px; height: 14px; border: 1px solid var(--black); position: relative; }
  .search-box svg { position: absolute; right: 6px; top: 3px; }

  /* Nav */
  .nav { left: 0; top: 112px; width: 1200px; height: 25px; background: var(--black); }
  .nav ul { list-style: none; position: absolute; left: 0; top: 0; width: 100%; height: 100%; }
  .nav li { position: absolute; top: 7px; font-family: var(--serif); font-size: 8.5px; color: var(--white); text-transform: uppercase; letter-spacing: 0.2px; white-space: nowrap; }

  /* Hero */
  .hero-photo { left: 276px; top: 147px; width: 409px; height: 264px; background: linear-gradient(180deg, #8aa26a 0%, #a4a78a 45%, #8d8470 75%, #b8b3a8 100%); }
  .hero-side { left: 685px; top: 147px; width: 231px; height: 264px; background: linear-gradient(160deg, #6f7a6e 0%, #8d968c 50%, #9aa092 100%); }
  .hero-words { left: 719px; top: 198px; font-family: var(--sans); color: var(--white); font-size: 36px; line-height: 44px; }

  /* Product cards */
  .card { width: 276px; height: 205px; overflow: hidden; }
  .card-photo { position: absolute; inset: 0; }
  .card-title { position: absolute; background: rgba(255,255,255,0.92); font-family: var(--serif); color: var(--copper); font-size: 19px; text-align: center; line-height: 26px; height: 26px; }
  .card-text { position: absolute; font-family: var(--sans); color: var(--white); font-size: 10px; line-height: 12.5px; }
  .card-actions { position: absolute; bottom: 18px; right: 15px; display: flex; gap: 12px; }
  .btn { display: block; background: var(--copper); color: var(--white); font-family: var(--sans); font-size: 8px; text-align: center; border-radius: 3px; }
  .card-actions .btn { width: 34px; height: 14px; line-height: 14px; }

  .oilskins { left: 305px; top: 427px; }
  .woollens { left: 611px; top: 427px; }
  .kids { left: 305px; top: 644px; }
  .hivis { left: 611px; top: 644px; }

  /* Story banner */
  .story-photo { left: 263px; top: 871px; width: 668px; height: 102px; background: linear-gradient(90deg, #5f8a2e 0%, #8fae55 35%, #b8bfa8 60%, #9fae7c 100%); }
  .story-text { left: 639px; top: 880px; width: 285px; font-family: var(--sans); color: var(--white); font-size: 11.5px; line-height: 15px; }

  /* Footer */
  .footer { left: 0; top: 973px; width: 1200px; height: 227px; background: var(--black); }
  .foot-links { font-family: var(--sans); color: var(--white); font-size: 10px; line-height: 12px; list-style: none; }
  .foot-links li { position: absolute; white-space: nowrap; }
  .partner-badge { left: 307px; top: 1156px; width: 146px; height: 31px; background: #3a3a3a; border: 2px solid #8a8a8a; }
  .signup { left: 589px; top: 989px; width: 327px; height: 132px; background: var(--copper-dark); }
  .signup p { position: absolute; left: 10px; top: 10px; width: 310px; font-family: var(--sans); color: var(--white); font-size: 11px; line-height: 15px; }
  .signup label { position: absolute; left: 18px; font-family: var(--sans); color: var(--white); font-size: 11.5px; }
  .signup .field { position: absolute; left: 118px; width: 195px; height: 20px; background: var(--white); border: 1px solid var(--black); }
  .refer { left: 643px; top: 1136px; font-family: var(--sans); color: var(--white); font-size: 11.5px; line-height: 15px; }
  .refer-btn { left: 723px; top: 1155px; width: 82px; height: 22px; line-height: 22px; font-size: 12px; border-radius: 3px; }
</style>
</head>
<body>

<header>
  <div class="brand abs"><span class="brand-dot"></span><span class="brand-name">COPPER RIDGE</span></div>
  <h1 class="tagline abs">Traditional oilskin &amp; woollen clothing</h1>
  <div class="offers abs">
    <div>Free delivery over $99 NZ wide</div>
    <div>Worldwide sales welcome</div>
    <div class="phone">0800 412 906</div>
  </div>
  <div class="search abs"><span>Search</span>
    <span class="search-box"><svg width="9" height="7" viewBox="0 0 9 7"><path d="M0 0h9L4.5 7z" fill="#000"/></svg></span>
  </div>
</header>

<nav class="nav abs">
  <ul>
    <li style="left:293px">Home</li>
    <li style="left:336px">About us</li>
    <li style="left:397px">Oilskin</li>
    <li style="left:447px">Wool</li>
    <li style="left:496px">Trousers</li>
    <li style="left:565px">Gift vouchers</li>
    <li style="left:653px">Emboirdery/Branding</li>
    <li style="left:767px">Costomer srvice</li>
    <li style="left:860px">Contact</li>
  </ul>
</nav>

<section class="hero">
  <div class="hero-photo abs" role="img" aria-label="Two young boys in oilskin vests standing on a gravel farm track by wooden fence posts"></div>
  <div class="hero-side abs" role="img" aria-label="Soft blurred green and grey farm landscape"></div>
  <div class="hero-words abs">Dry<br>Protective<br>Comfy</div>
</section>

<section class="products">
  <article class="card oilskins abs">
    <div class="card-photo" role="img" aria-label="Young man in a wide-brim hat and oilskin jacket on green hills" style="background:linear-gradient(160deg,#6f9a4a 0%,#8aa56a 45%,#6b6a5a 100%)"></div>
    <h2 class="card-title" style="left:61px;top:7px;width:155px">Oilskins</h2>
    <p class="card-text" style="left:150px;top:47px;width:116px">Short sleeve and sleeveless hi vis oilskin vests protection from the elements whil being seen. Ask us abot our monogramming service.</p>
    <div class="card-actions"><span class="btn">View</span><span class="btn">Buy</span></div>
  </article>

  <article class="card woollens abs">
    <div class="card-photo" role="img" aria-label="Woollen socks, hat and gloves laid on a wooden rail" style="background:linear-gradient(180deg,#7a7470 0%,#8d8a86 50%,#6e6660 100%)"></div>
    <p class="card-text" style="left:56px;top:5px;width:200px">Get kitted out with all your winter woollen clothing – gloves, hats, singlets, tees and jerseys. Ask us about our monogramming service.</p>
    <h2 class="card-title" style="left:69px;top:132px;width:153px">Woollen clothing</h2>
    <div class="card-actions"><span class="btn">View</span><span class="btn">Buy</span></div>
  </article>

  <article class="card kids abs">
    <div class="card-photo" role="img" aria-label="Two small boys in oilskin vests and gumboots on a gravel track" style="background:linear-gradient(170deg,#8a9a6a 0%,#9e9a88 45%,#7d7668 100%)"></div>
    <h2 class="card-title" style="left:60px;top:0;width:156px">Kids’ oilskins</h2>
    <p class="card-text" style="left:157px;top:52px;width:118px">Be just like the grown-ups ! Sizes 2 to 14 kids’ oilskin sleeveless vests. Keep warm outside!<br>Ask us about our monogramming service.</p>
    <div class="card-actions"><span class="btn">View</span><span class="btn">Buy</span></div>
  </article>

  <article class="card hivis abs">
    <div class="card-photo" role="img" aria-label="Farm worker in a hi-vis oilskin vest crouching near grain silos" style="background:linear-gradient(160deg,#a8b0b0 0%,#8c9088 45%,#6f6656 100%)"></div>
    <h2 class="card-title" style="left:72px;top:6px;width:135px">Hi-vis oilskins</h2>
    <p class="card-text" style="left:157px;top:47px;width:118px">Short sleeve and sleeveless hi vis oilskin vests protection from the elements while being seen. Ask us about our monogramming service.</p>
    <div class="card-actions"><span class="btn">View</span><span class="btn">Buy</span></div>
  </article>
</section>

<section class="story">
  <div class="story-photo abs" role="img" aria-label="Green rolling New Zealand farmland"></div>
  <p class="story-text abs">Copper Ridge is a Southland family-owned business.<br>All oilskin and woollen clothing is 100% New Zealand made.<br>More keyworded text in this area about the brand and the business…</p>
</section>

<footer class="footer abs">
  <ul class="foot-links">
    <li style="left:296px;top:18px">Home</li>
    <li style="left:296px;top:43px">About Us<br>--Testimonials</li>
    <li style="left:296px;top:82px">Gift Vouchers</li>
    <li style="left:296px;top:108px">Embroidery/Branding</li>
    <li style="left:296px;top:134px">Customer Service</li>
    <li style="left:296px;top:160px">Contact/Map</li>
    <li style="left:417px;top:15px">Oilskin<br>---Vest<br>---Jackets<br>---Hi-viz</li>
    <li style="left:417px;top:79px">Wool<br>---erseys<br>---Singlets<br>---Socks<br>---Gloves</li>
    <li style="left:417px;top:161px">Trousers</li>
  </ul>
  <form class="signup abs" style="top:16px">
    <p>Sign up to get our regular but occasional email letting you know what the latest news and deals are with Copper Ridge…</p>
    <label style="top:69px">First Name</label><span class="field" style="top:62px"></span>
    <label style="top:103px">Email Address</label><span class="field" style="top:96px"></span>
  </form>
</footer>
<div class="partner-badge abs" aria-label="Partner badge"></div>
<p class="refer abs">Refer the Copper Ridge website to a friend:<br>Click here</p>
<span class="btn refer-btn abs">Click</span>

</body>
</html>
```